Ski Lodge Website update

We need to revamp our website http://www.tbr-lodge.org.au to reflect HTML5, larger, beautiful fonts, drop-down menu navigation (no more navigation on left side), addthis twitter/facebook/google+ integration and more, with a twitter feed down the side of the home page (but not on other pages), and great high-res images in a scrolling gallery at the base of the page, with a high-res background.

The current logo is to remain unchanged.

Only images from our own gallery folder can be used - http://www.tbr-lodge.org.au/gallery

Requirements
Must have
• MUST be mobile accessible.
• Resulting images and css must be cut and ready for deployment on existing side, to replace existing headers/footers and sidebars.
Nice to have
• Jquery or other js to link offsite (e.g. to google)

```html
<!DOCTYPE html>
<html lang="en">
<head>
<meta charset="utf-8">
<title>Timber Ridge Lodge – Mt Aldermoor</title>
<link href="https://fonts.googleapis.com/css2?family=Source+Sans+3:wght@300;400;600;700&display=swap" rel="stylesheet">
<style>
:root{
  --red:#d8000b;
  --yellow:#ffe400;
  --ink:#111;
  --body:#555;
  --rule:#bdbdbd;
  --button:#8c8c8c;
  --footer:#ececec;
  --page:#fbfbfb;
  --panel-edge:#d6d6d6;
  --font:"Source Sans 3",sans-serif;
}
*{margin:0;padding:0;box-sizing:border-box}
html,body{width:1200px;height:1170px;overflow:hidden}
body{position:relative;background:var(--page);font-family:var(--font);color:var(--ink)}
a{color:inherit;text-decoration:none}

.site-header{position:absolute;left:0;top:0;width:1200px;height:102px;background:#fff}
.brand{position:absolute;left:119px;top:0;width:165px;height:214px;z-index:3}
.brand-name{position:absolute;left:30px;top:52px;width:110px;font-size:12px;font-weight:600;letter-spacing:2px;line-height:19px;color:#333;text-transform:uppercase}
.booking{position:absolute;right:130px;top:17px;font-size:20px;font-weight:700;color:var(--red)}
.booking span{margin-left:10px}
.main-nav{position:absolute;right:129px;top:59px;display:flex;gap:44px;font-size:20px;font-weight:300;color:#333}

.hero{position:absolute;left:0;top:102px;width:1200px;height:331px;
  background:linear-gradient(180deg,#3b78c4 0%,#8fb4dc 30%,#d8dfe6 55%,#eef1f4 75%,#f6f7f8 100%)}
.hero-dots{position:absolute;left:562px;top:399px;display:flex;gap:5px}
.hero-dots i{width:15px;height:15px;border-radius:50%;background:#fff;display:block}
.hero-dots i.on{background:var(--red)}

.tagline{position:absolute;left:0;top:453px;width:1200px;text-align:center;font-size:25px;font-weight:300;color:var(--red)}
.welcome{position:absolute;left:0;top:509px;width:1160px;text-align:center;font-size:19px;font-weight:600}
.intro{position:absolute;left:127px;top:548px;width:942px;text-align:center;font-size:15.6px;font-weight:300;line-height:24px;color:var(--body)}

.col-title{position:absolute;font-size:19px;font-weight:600;height:39px;border-bottom:1px solid var(--rule)}
.tweet{position:absolute;left:128px;width:300px}
.tweet .dot{position:absolute;left:2px;top:4px;width:14px;height:14px;border-radius:50%;background:#29a9e1}
.tweet p{margin-left:38px;font-size:12.5px;font-weight:300;line-height:22px;color:#444}

.photo{position:absolute}
.arrow{position:absolute;top:796px}

.special{position:absolute;left:770px;top:654px;width:298px;height:213px;background:var(--red);overflow:hidden}
.special .lead{position:absolute;left:9px;top:12px;font-size:18px;font-weight:300;color:#fff}
.special .price{position:absolute;left:14px;top:35px;font-size:24px;font-weight:700;color:var(--yellow)}
.special .room{position:absolute;left:0;top:70px;width:298px;height:143px;background:linear-gradient(135deg,#6b4a37 0%,#a57858 40%,#d9cfc4 60%,#7a2130 100%)}
.special .note{position:absolute;left:0;top:118px;width:210px;height:78px;background:rgba(40,40,40,.6);padding:5px 4px;color:#fff;font-size:11px;font-weight:300;line-height:18px}
.special .note b{display:block;font-size:14px;font-weight:700;margin-top:2px}

.testimonials h3{position:absolute;left:765px;top:877px;font-size:19px;font-weight:600}
.quote{position:absolute;left:766px;top:919px;width:300px;font-size:12.5px;font-weight:300;line-height:22px;color:#444;padding-left:6px}
.byline{position:absolute;left:773px;top:970px;font-size:14px;font-weight:300}

.cta{position:absolute;top:1009px;width:295px;height:61px;background:var(--button);color:#fff;font-size:20px;font-weight:700;text-transform:uppercase;display:flex;align-items:center;justify-content:center}

.site-footer{position:absolute;left:0;top:1086px;width:1200px;height:84px;background:var(--footer)}
.foot-nav{position:absolute;left:132px;top:14px;font-size:15px;font-weight:300;display:flex}
.foot-nav a+a::before{content:"|";margin:0 17px}
.copyright{position:absolute;left:132px;top:48px;font-size:15px;font-weight:300}
.social{position:absolute;top:16px;width:35px;height:35px;border-radius:50%}
</style>
</head>
<body>

<header class="site-header">
  <div class="brand">
    <svg width="165" height="214" viewBox="0 0 165 214" aria-hidden="true">
      <path d="M0 0H165V203L82 188L0 208Z" fill="#fff"/>
      <path d="M0 206L82 188L165 205V214L82 196L0 214Z" fill="var(--panel-edge)"/>
    </svg>
    <div class="brand-name">Timber<br>Ridge<br>Lodge</div>
  </div>
  <div class="booking">Booking phone:<span>0400 555 123</span></div>
  <nav class="main-nav">
    <a href="#">Home</a><a href="#">Rates</a><a href="#">Location</a><a href="#">Facilities</a><a href="#">Member Login</a><a href="#">Contact Us</a>
  </nav>
</header>

<section class="hero" role="img" aria-label="Panoramic photo of the snow-covered ski village with skiers and lodges under a blue sky"></section>
<div class="hero-dots"><i class="on"></i><i></i><i></i><i></i></div>

<h1 class="tagline">A great alpine holiday experience in one of aldermoor's best ski lodges</h1>
<h2 class="welcome">Welcome to Our Website</h2>
<p class="intro">The ideal Mt Aldermoor accommodation for your snow holiday. The Timber Ridge Ski Lodge is multi-level, modern, comfortable and well appointed. Mt Aldermoor Village facilities, transport, ski lifts and shops are all nearby.The spacious lounge and dining areas have breathtaking views of the alps surrounding Mt Aldermoor. There's a games room, new modern kitchen with barbecue, an open fire, a large balcony, guest laundry, drying room and ski room.</p>

<h3 class="col-title" style="left:129px;top:654px;width:300px">Recent Tweets</h3>
<div class="tweet" style="top:706px"><span class="dot"></span><p>Velit esse cillum dolore eu fugiat nulla pariatur. Excepteur sint occaecat cupidatat non proident. @SnowlineNotes #EnjeuSanté</p></div>
<div class="tweet" style="top:816px"><span class="dot"></span><p>Velit esse eu fugiat nulla pariatur. Excepteur sint occaecat cupidatat non proident.<br>@SnowlineNotes #EnjeuSanté"</p></div>
<div class="tweet" style="top:926px"><span class="dot"></span><p>Velit esse cillum dolore eu fugiat nulla pariatur. Excepteur sint occaecat cupidatat non proident. @SnowlineNotes #EnjeuSanté</p></div>

<h3 class="col-title" style="left:448px;top:654px;width:301px">Photo Gallery</h3>
<div class="photo" style="left:449px;top:711px;width:300px;height:185px;background:linear-gradient(160deg,#c9a46a 0%,#e8d7b8 30%,#6f7d86 60%,#dfe6ee 85%,#f3f5f8 100%)" role="img" aria-label="Snow-laden pine trees at sunset"></div>
<svg class="arrow" style="left:458px" width="26" height="26" viewBox="0 0 26 26" aria-hidden="true"><circle cx="13" cy="13" r="12.5" fill="#fff"/><path d="M15 7L9 13L15 19" fill="none" stroke="#555" stroke-width="2.5"/></svg>
<svg class="arrow" style="left:713px" width="26" height="26" viewBox="0 0 26 26" aria-hidden="true"><circle cx="13" cy="13" r="12.5" fill="#fff"/><path d="M11 7L17 13L11 19" fill="none" stroke="#555" stroke-width="2.5"/></svg>
<div class="photo" style="left:449px;top:912px;width:94px;height:73px;background:linear-gradient(180deg,#b9cde0,#e9edf1 60%,#8a9099)" role="img" aria-label="Snowy slopes thumbnail"></div>
<div class="photo" style="left:551px;top:912px;width:94px;height:73px;background:linear-gradient(180deg,#5c6470,#a9b4c0 50%,#eef0f2)" role="img" aria-label="Chairlift station with skiers thumbnail"></div>
<div class="photo" style="left:654px;top:912px;width:94px;height:73px;background:linear-gradient(180deg,#2f5fa8,#8aa7cf 50%,#e6ecf4)" role="img" aria-label="Snowy village at dusk thumbnail"></div>

<aside class="special">
  <div class="lead">Room rate special from</div>
  <div class="price">$208 per night!</div>
  <div class="room" role="img" aria-label="Lodge guest room with beds and desk"></div>
  <div class="note">Adults stay at kids prices when full room booked mid-week for 3 or more nights!<b>Click here!</b></div>
</aside>

<section class="testimonials">
  <h3>Testimonials</h3>
  <p class="quote">“ Lorem Ipsum is simply dummy text of the printing and typesetting industry. ”</p>
  <p class="byline">By.Mara Ellison</p>
</section>

<a class="cta" href="#" style="left:129px">How to Join</a>
<a class="cta" href="#" style="left:451px">Luggage Transport</a>
<a class="cta" href="#" style="left:772px">Partners Offers</a>

<footer class="site-footer">
  <nav class="foot-nav">
    <a href="#">Home</a><a href="#">Rates</a><a href="#">Location</a><a href="#">Facilities</a><a href="#">Member Login</a><a href="#">Contact Us</a>
  </nav>
  <p class="copyright">Copyright ©2013 &nbsp;Company Name &nbsp;&nbsp;&nbsp;- All rights reserved</p>
  <a class="social" href="#" aria-label="Follow us" style="left:990px;background:#7cc6ec"></a>
  <a class="social" href="#" aria-label="Like us" style="left:1033px;background:#3b65ad"></a>
</footer>

</body>
</html>
```